Innovative and exciting banner advert for real estate
Lots of freedom of design
#10 I like the way the 'save thousands in commission' is done with mixed size font. The 'save thousands' stands out very clearly which is important to us
Thanks.
Hi and thank you designers for your attention to our project, there are some great ideas coming in now.
A slight change to the brief:
In the blue screen, please remove 'money back guarantee' and replace with 'no hidden charges' from the green screen so each screen has only 3 bullet points.
Thanks
RPellow
Hi Designers
Please note, we do not require the logo in the adverts just the use of the logo colours as the base.
It is more important that the first line of text stands out. If you are going to insert the logo, please make it a minor element or as #4 has cleverly used it for the bullet points.
Thanks designers for your time and great ideas. #4 I like the way you have used the logo symbol in the bullet points, and that you have aligned the bullets points to the left, it looks good.
#5 the way that 'save thousands' and 'get the best price' stand out clearly is great, this is the message that we are trying to pass on to viewers, it is most important.
If there is any information you need please contact me directly, I will check messages.
Just to clarify, we do not require the logo in the adverts just the use of the logo colours as the base. These adverts are going to be used on our own site.
Regards
Thanks Hostmod for making that clear for designers.
Designers, we don't have images of the product we sell as we provide real estate services (not goods). If looking for inspiration for imagery, residential property is more appropriate than commercial property.
Thanks everyone.
Attention Designers!
PH is looking for static banner design which includes two individual advert frames.
Banner size : 450 wide x 225 high
I'm clarifying with our site technicians exactly what the frames should be.
We originally wanted two individual advert frames, 450 wide x 225 high, with no animation in the frames themselves. However, when trying to work within the Tandelvox fields, we couldn't elect the specific size we required and instead had to opt for a package deal.
I will upload a link to the real estate website template we will be using, the template has 'featured property' images in the centre of the homepage which we will be replacing with our two adverts. That is, we will not have the featured property on the home page at all.
http://skins.brovellanstudio.example/?theme=realestate2
Dear PH,
Is this animated gifs or flash?

```html
<!DOCTYPE html>
<html lang="en">
<head>
<meta charset="utf-8">
<title>Keyfold Property – Save Thousands in Commission</title>
<link href="https://fonts.googleapis.com/css2?family=Anton&family=Oswald:wght@600;700&display=swap" rel="stylesheet">
<style>
  :root {
    --sky-white: #ffffff;
    --blue-deep: #0f4c9e;
    --blue-mid: #1f6cc4;
    --blue-light: #3a93e0;
    --blue-fringe: #8cc4ee;
    --navy-band: #0a2b63;
    --brand-blue: #1565c0;
    --tick-green: #7cc242;
    --text-white: #ffffff;
  }
  html, body {
    margin: 0;
    padding: 0;
    width: 1200px;
    height: 600px;
    overflow: hidden;
    background: var(--blue-deep);
  }
  .banner {
    position: relative;
    width: 1200px;
    height: 600px;
    overflow: hidden;
    background: radial-gradient(ellipse 70% 80% at 50% 60%, var(--blue-light) 0%, var(--blue-mid) 45%, var(--blue-deep) 100%);
    font-family: "Oswald", "Arial Narrow", sans-serif;
  }
  .banner-top {
    position: absolute;
    inset: 0 0 auto 0;
    width: 1200px;
    height: 200px;
  }
  .brand {
    position: absolute;
    top: 22px;
    left: 0;
    width: 1200px;
    display: flex;
    justify-content: center;
    align-items: center;
    gap: 22px;
  }
  .brand-square {
    width: 84px;
    height: 84px;
    background: var(--brand-blue);
  }
  .brand-name {
    font-family: "Anton", "Impact", sans-serif;
    font-size: 78px;
    line-height: 1;
    color: var(--brand-blue);
    letter-spacing: 1px;
    text-transform: uppercase;
  }
  .headline-band {
    position: absolute;
    top: 170px;
    left: 0;
    width: 1200px;
    height: 96px;
    background: var(--navy-band);
    border-top: 3px solid var(--blue-fringe);
    display: flex;
    align-items: center;
    justify-content: center;
  }
  .headline {
    margin: 0;
    font-family: "Anton", "Impact", sans-serif;
    font-weight: 400;
    line-height: 1;
    color: var(--text-white);
    letter-spacing: 1px;
    text-transform: uppercase;
    white-space: nowrap;
  }
  .headline-lead {
    font-size: 86px;
  }
  .headline-rest {
    font-size: 58px;
  }
  .benefits {
    position: absolute;
    top: 310px;
    left: 0;
    width: 1200px;
    margin: 0;
    padding: 0;
    list-style: none;
    display: flex;
    flex-direction: column;
    align-items: center;
    gap: 10px;
  }
  .benefit {
    display: flex;
    align-items: center;
    gap: 16px;
    font-weight: 700;
    font-size: 50px;
    line-height: 58px;
    color: var(--text-white);
    text-transform: uppercase;
    letter-spacing: 0.5px;
    white-space: nowrap;
  }
  .tick {
    width: 44px;
    height: 44px;
    flex: none;
  }
  .banner-foot {
    position: absolute;
    left: 0;
    bottom: 0;
    width: 1200px;
    height: 40px;
    background: linear-gradient(180deg, var(--blue-mid), var(--blue-light));
  }
</style>
</head>
<body>
  <div class="banner">
    <svg class="banner-top" viewBox="0 0 1200 200" aria-hidden="true">
      <path d="M0 0 H1200 V150 Q600 185 0 150 Z" fill="var(--blue-fringe)"/>
      <path d="M0 0 H1200 V138 Q600 170 0 138 Z" fill="var(--sky-white)"/>
    </svg>

    <div class="brand">
      <span class="brand-square"></span>
      <span class="brand-name">Keyfold Property</span>
    </div>

    <div class="headline-band">
      <h1 class="headline"><span class="headline-lead">Save Thousands</span> <span class="headline-rest">in Commission</span></h1>
    </div>

    <ul class="benefits">
      <li class="benefit">
        <svg class="tick" viewBox="0 0 44 44" aria-hidden="true"><circle cx="22" cy="22" r="21" fill="var(--tick-green)"/><path d="M12 23 L19 30 L32 15" fill="none" stroke="#fff" stroke-width="5" stroke-linecap="round" stroke-linejoin="round"/></svg>
        Private Property Sales Solutions
      </li>
      <li class="benefit">
        <svg class="tick" viewBox="0 0 44 44" aria-hidden="true"><circle cx="22" cy="22" r="21" fill="var(--tick-green)"/><path d="M12 23 L19 30 L32 15" fill="none" stroke="#fff" stroke-width="5" stroke-linecap="round" stroke-linejoin="round"/></svg>
        Assisted Property Sales Expertise
      </li>
      <li class="benefit">
        <svg class="tick" viewBox="0 0 44 44" aria-hidden="true"><circle cx="22" cy="22" r="21" fill="var(--tick-green)"/><path d="M12 23 L19 30 L32 15" fill="none" stroke="#fff" stroke-width="5" stroke-linecap="round" stroke-linejoin="round"/></svg>
        No Hidden Charges
      </li>
    </ul>

    <div class="banner-foot"></div>
  </div>
</body>
</html>
```